terras letterhead

We would like to create a new letterhead that our company will use for proposals, invoices, statements and letters. Our company name is Terra-Crafters. We are a landscape design/build and landscape maintenance company. We have a web site Terra-Crafters.example where our logo (the leaf with the lettering within it only) is displayed.

Industry/Entity Type

Graphic Design

Requirements
Must have
• Address and info on our current letterhead (uploaded)
Nice to have
• We would like the design to look presentable in grey scale as well as color.
Should not have
• Do not want to infringe much on the normal useable area within the normal print areas.

```html
<!DOCTYPE html>
<html lang="en">
<head>
<meta charset="utf-8">
<title>Terra-Crafters Letterhead</title>
<link href="https://fonts.googleapis.com/css2?family=Arimo:wght@400&family=Quicksand:wght@400;600&display=swap" rel="stylesheet">
<style>
  :root {
    --backdrop: #0f5a2c;
    --paper: #ffffff;
    --brand-green: #1d4722;
    --ink: #1a1a1a;
    --mark-grey: #dcdcdc;
  }
  * { margin: 0; padding: 0; box-sizing: border-box; }
  html, body {
    width: 1200px; height: 848px; overflow: hidden;
    background: var(--backdrop);
  }
  .canvas { position: relative; width: 1200px; height: 848px; }
  .letterhead {
    position: absolute; left: 320px; top: 27px;
    width: 560px; height: 795px;
    background: var(--paper); overflow: hidden;
  }
  .margin-rule {
    position: absolute; left: 40px; width: 4px;
    background: var(--brand-green);
  }
  .margin-rule--top { top: 21px; height: 70px; }
  .margin-rule--bottom { top: 122px; height: 629px; }
  .brand-name {
    position: absolute; left: 26px; top: 92px;
    display: flex; align-items: center; gap: 7px;
    font-family: "Arimo", sans-serif; font-size: 13px;
    letter-spacing: 0.5px; color: var(--brand-green);
  }
  .brand-square { width: 9px; height: 9px; background: var(--brand-green); }
  .letter-body {
    position: absolute; left: 71px; top: 175px; width: 456px;
    font-family: "Arimo", sans-serif; font-size: 8.1px;
    line-height: 11.25px; color: var(--ink);
    text-align: justify; hyphens: auto;
  }
  .letter-body p + p { margin-top: 11.25px; }
  .signature {
    position: absolute; left: 70px; top: 532px;
    width: 145px; height: 32px;
    background: linear-gradient(90deg, #e6e6e6, #f4f4f4);
    border-radius: 3px;
  }
  .faint-mark {
    position: absolute; right: 0; top: 528px;
    width: 235px; height: 165px;
    background: radial-gradient(ellipse at 70% 40%, #d6d6d6, #ececec 70%, rgba(255,255,255,0) 100%);
  }
  .contact-footer {
    position: absolute; left: 0; right: 0; top: 719px;
    text-align: center;
    font-family: "Quicksand", sans-serif; font-size: 7.6px;
    line-height: 13.5px; color: var(--ink);
  }
  .contact-footer b { font-weight: 600; }
</style>
</head>
<body>
<div class="canvas">
  <article class="letterhead">
    <div class="margin-rule margin-rule--top"></div>
    <div class="margin-rule margin-rule--bottom"></div>

    <div class="brand-name"><span class="brand-square"></span>Terra-Crafters</div>

    <div class="letter-body">
      <p>Lorem ipsum dolor sit amet, consectetur adipiscing elit. Suspendisse blandit, nulla ut porta scelerisque, urna massa ultrices ligula, at rutrum nunc ipsum ac risus. Sed consectetur nulla non velit sollicitudin a eleifend tortor pellentesque. Cras laoreet iaculis pretium. Vestibulum vitae sapien at metus fermentum tempus quis sed mauris. Donec blandit metus in nibh laoreet ultrices. Nullam molestie, turpis ac adipiscing tincidunt, urna justo eleifend ligula, et consectetur massa lorem ac risus. Aenean quis justo vitae massa accumsan ultricies posuere eget diam. Aenean ipsum sapien, pellentesque id semper vitae, mattis eget enim. Vestibulum congue tincidunt enim ut tristique. Praesent interdum malesuada adipiscing. Donec quis felis massa.</p>
      <p>Praesent nisi libero, pretium eu interdum eu, rhoncus ut lorem. Praesent faucibus lorem sit amet ligula consequat adipiscing. Morbi adipiscing dapibus erat, eu condimentum nibh vestibulum vel. In elementum nulla id arcu bibendum malesuada. Donec non nulla sit amet tortor volutpat placerat id vel felis. Maecenas accumsan, augue ac molestie iaculis, justo risus vestibulum dolor, eu ullamcorper nulla orci ac est. Donec tristique sem a nisl euismod convallis id ac lacus. Sed pretium bibendum velit eget mollis. Praesent porta suscipit lacus, ac porta odio faucibus eu. Donec accumsan laoreet nisi et hendrerit. In fringilla enim ac urna sagittis convallis.</p>
      <p>Nullam est mi, euismod ac pretium ac, consequat eu urna. Aliquam egestas, elit non gravida pellentesque, purus orci facilisis est, vitae ultricies turpis nisl non justo. Fusce varius libero nec nibh elementum consequat ut sed elit. Integer lorem erat, varius ac malesuada vitae, convallis sit amet libero. Cras sagittis, urna eu scelerisque auctor, elit tellus vestibulum mi, non elementum metus eros ut dolor. Etiam porta est dolor. Vivamus suscipit lobortis commodo. Integer convallis, nunc tincidunt rhoncus lobortis, sapien purus ultrices orci, quis dignissim urna felis dictum elit.</p>
    </div>

    <div class="signature" role="img" aria-label="Handwritten signature of Marco Bellini"></div>

    <div class="faint-mark" role="img" aria-label="Faint grey brand mark decoration"></div>

    <footer class="contact-footer">
      <div>218 Meadowbrook Lane &nbsp;- &nbsp;Fernhill, NJ 07190</div>
      <div><b>t.</b> (555) 014-2231 &nbsp;- <b>f.</b> (555) 014-2290</div>
      <div><b>e.</b> service@terra-crafters.example &nbsp;<b>w.</b> www.terra-crafters.example</div>
    </footer>
  </article>
</div>
</body>
</html>
```